Velmarin is a skin care brand, currently selling in India. We want to make design for our new la...

We want to develop label design for our new launch sunscreen . It is Anti-pollution sunscreen with SPF 50

Colors

Designer to choose colors to be used in the design.

```html
<!DOCTYPE html>
<html lang="en">
<head>
<meta charset="utf-8">
<title>Velmarin Anti-Pollution Sunscreen SPF 50 – Label</title>
<link href="https://fonts.googleapis.com/css2?family=Barlow+Semi+Condensed:wght@500;600&family=Barlow:wght@600&display=swap" rel="stylesheet">
<style>
  :root{
    --sun-yellow:#f8c21c;
    --sun-light:#fde89a;
    --sun-orange:#f39a12;
    --label-white:#ffffff;
    --brand-blue:#1b2b9e;
    --brand-blue-deep:#14207f;
    --accent-yellow:#f6ec00;
    --aloe-green:#3f8f2a;
    --aloe-light:#8cc63f;
  }
  html,body{margin:0;padding:0;overflow:hidden}
  body{width:742px;height:1200px;background:#eeeeee}
  .label{
    position:relative;width:742px;height:1200px;overflow:hidden;
    background:linear-gradient(180deg,var(--sun-yellow) 0%,var(--sun-light) 30%,#fff6d8 58%,var(--label-white) 75%,var(--label-white) 100%);
    font-family:"Barlow Semi Condensed",sans-serif;color:var(--brand-blue);
  }
  .waves{position:absolute;left:0;top:0;width:742px;height:1200px}
  .brand{
    position:absolute;left:170px;top:300px;width:402px;height:84px;
    background:var(--brand-blue-deep);display:flex;align-items:center;justify-content:center;
  }
  .brand-name{
    font-family:"Barlow",sans-serif;font-weight:600;font-size:60px;letter-spacing:2px;
    color:var(--label-white);text-transform:uppercase;line-height:1;
  }
  .product-type{position:absolute;left:0;width:742px;top:430px;text-align:center;line-height:1}
  .product-type .kicker{display:block;font-weight:600;font-size:46px;letter-spacing:.5px}
  .product-type .name{display:block;font-weight:600;font-size:68px;margin-top:4px}
  .spf{
    position:absolute;left:185px;top:560px;width:372px;height:110px;
    background:var(--brand-blue);color:var(--label-white);
    font-weight:600;font-size:88px;display:flex;align-items:center;justify-content:center;
  }
  .spf-underline{position:absolute;left:185px;top:670px;width:372px;height:20px;background:var(--accent-yellow)}
  .aloe{
    position:absolute;left:390px;top:540px;width:320px;height:620px;
    background:radial-gradient(ellipse at 60% 60%,var(--aloe-light) 0%,var(--aloe-green) 55%,rgba(63,143,42,0) 75%);
  }
  .claims{position:absolute;left:70px;top:860px;margin:0;padding:0;list-style:none}
  .claim{display:flex;gap:10px;font-weight:500;font-size:34px;line-height:1.15;margin-bottom:38px}
  .claim svg{flex:none;margin-top:4px}
  .volume{position:absolute;left:0;width:742px;top:1110px;text-align:center;font-weight:500;font-size:36px}
</style>
</head>
<body>
<div class="label">
  <svg class="waves" viewBox="0 0 742 1200" aria-hidden="true">
    <path d="M0 430 C120 520 60 760 220 820 C360 870 520 760 742 700 L742 760 C540 820 380 930 220 900 C60 870 80 640 0 560 Z" fill="#f6a21a" opacity=".55"/>
    <path d="M0 560 C70 660 90 860 260 880 C420 900 560 820 742 780 L742 820 C560 860 420 950 250 930 C80 910 40 700 0 640 Z" fill="#ffffff" opacity=".45"/>
  </svg>

  <div class="brand"><span class="brand-name">Velmarin</span></div>

  <h1 class="product-type" style="margin:0">
    <span class="kicker">ANTI-POLLUTION</span>
    <span class="name">SUNSCREEN</span>
  </h1>

  <div class="spf">SPF 50</div>
  <div class="spf-underline"></div>

  <div class="aloe" role="img" aria-label="Illustration of fresh aloe vera leaves with water droplets"></div>

  <ul class="claims">
    <li class="claim">
      <svg width="30" height="30" viewBox="0 0 30 30" aria-hidden="true"><circle cx="14" cy="16" r="11" fill="none" stroke="var(--brand-blue)" stroke-width="3"/><path d="M8 15 l6 6 L27 3" fill="none" stroke="var(--brand-blue)" stroke-width="3.5" stroke-linecap="round"/></svg>
      <span>Enriched<br>with Aloe-Vera</span>
    </li>
    <li class="claim">
      <svg width="30" height="30" viewBox="0 0 30 30" aria-hidden="true"><circle cx="14" cy="16" r="11" fill="none" stroke="var(--brand-blue)" stroke-width="3"/><path d="M8 15 l6 6 L27 3" fill="none" stroke="var(--brand-blue)" stroke-width="3.5" stroke-linecap="round"/></svg>
      <span>Protection against<br>pollutant particles<br>up to 2.5 microns</span>
    </li>
  </ul>

  <div class="volume">88 ml</div>
</div>
</body>
</html>
```